Premium Corporate Website Design for Velmora Systems

Our company Velmora Systems GmbH (formerly BrightHarbor GmbH) is looking for a new, modern, and professional corporate website. The content should be based on our existing site bright-harbor.example
, but reimagined in a contemporary, tech-oriented, and premium design.

Requirements:

- Alignment with the new Velmora Systems logo and corporate identity
- Modern layout that reflects the tech and IT consulting industry
- Clear and user-friendly structure with intuitive navigation
- Premium look and feel that highlights our market position
- Incorporation of animated or interactive elements to add dynamism
- Design should clearly stand out from competitors such as Durlak GmbH, TMPulse, Vorndal, Marvix, and Holtreuven
- International focus: Since our company also operates in the U.S. market, the website should reflect a global presence (e.g., bilingual structure in German/English, international visual language, U.S.-inspired corporate design elements)

Goal:
To create a high-quality, innovative, and brand-strong website that positions Velmora Systems GmbH as a modern, trustworthy, and future-oriented IT consulting company — both in the German-speaking region and in the United States.

In addition to the design, we would also like the website to be delivered as functional HTML/CSS files (or WordPress implementation if possible).

All images from our current website www.bright-harbor.example
can be used if needed. Designers are welcome to reuse or adapt this material where appropriate."

Target Market(s)

Medium to large enterprises in the technology, finance, and energy sectors Companies seeking premium IT consulting, quality assurance, and test automation services Decision makers and executives (CIOs, CTOs, IT managers) in Europe and the United States A global audience that values innovation, professionalism, and trust

Industry/Entity Type

Information Technology & Consulting Software Testing & Quality Assurance Technology / Professional Services

Coding

Number of Pages Required

Requirements
Must have
• - Integration of the Velmora Systems logo and corporate identity - Bilingual setup (German & English) Modern, premium tech design with a professional look and feel Clear structure and intuitive navigation for easy usability Responsive design, optimized for desktop, tablet, and mobile High-quality visuals and dynamic elements (animations, interactive features) Strong differentiation from competitors (Durlak GmbH, TMPulse, Vorndal, Marvix, Holtreuven)
Nice to have
• Subtle micro-animations and hover effects to enhance user experience Custom icons or illustrations that align with the Velmora brand Dark/Light mode toggle for modern usability Blog or insights section to share expertise and updates SEO-friendly structure for better visibility in search engines Integration of social media feeds (LinkedIn, Facebook, Instagram) Contact form with automation (e.g., PHPMailer or CRM integration) Showcasing case studies or success stories with an engaging layout
Should not have
• Overly crowded or cluttered layouts Stock images that look generic or low quality Outdated design styles (e.g., gradients from the 2000s, heavy drop shadows) Complex navigation that confuses users Excessive use of bright or non-brand colors outside the Velmora identity Long loading times caused by oversized media files Pop-ups or intrusive ads that disrupt the premium brand image

```html
<!DOCTYPE html>
<html lang="en">
<head>
<meta charset="utf-8">
<title>Velmora Systems GmbH</title>
<link href="https://fonts.googleapis.com/css2?family=Lexend+Exa:wght@300;400;600;700&family=Inter:wght@400;500;600;700&display=swap" rel="stylesheet">
<style>
:root{
  --blue:#1d4fd8;
  --navy:#0a2a8a;
  --deep:#061c6e;
  --green:#35e24a;
  --teal:#19a7a3;
  --ink:#1b1f2a;
  --muted:#5d6370;
  --line:#e3e6ec;
  --field:#eef0f3;
  --mat:#e9e9ea;
  --btn:linear-gradient(90deg,#1769d6 0%,#22c7a0 60%,#35e24a 100%);
}
*{box-sizing:border-box;margin:0;padding:0}
html,body{width:1200px;height:4424px;overflow:hidden}
body{background:var(--mat);font-family:"Inter",sans-serif;color:var(--ink);position:relative}
.page{position:absolute;left:31px;top:27px;width:1133px;height:4348px;background:#fff;overflow:hidden}
.abs{position:absolute}
.heading{font-family:"Lexend Exa",sans-serif;font-weight:300;color:var(--ink);letter-spacing:-1px}
.btn{position:absolute;display:flex;align-items:center;justify-content:center;border-radius:20px;background:var(--btn);color:#fff;font-family:"Lexend Exa",sans-serif;font-weight:600;font-size:12px;letter-spacing:-.3px}

/* hero */
.hero{position:absolute;left:0;top:0;width:1133px;height:574px;background:linear-gradient(120deg,#0b3aa8 0%,#1557d0 45%,#0d3fb0 100%)}
.hero-photo{position:absolute;left:515px;top:0;width:618px;height:574px;background:radial-gradient(ellipse at 55% 45%,rgba(210,220,235,.55) 0%,rgba(40,90,200,.25) 45%,rgba(13,63,176,0) 75%)}
.nav{position:absolute;left:227px;top:14px;width:681px;height:45px;background:#fff;border-radius:23px;display:flex;align-items:center;padding:0 22px}
.brand{display:flex;align-items:center;gap:8px;font-family:"Lexend Exa",sans-serif;font-weight:600;font-size:13px;color:var(--navy)}
.brand-dot{width:16px;height:16px;border-radius:50%;background:var(--green)}
.nav ul{list-style:none;display:flex;gap:18px;margin-left:auto;font-size:9.5px;color:#8a90a0}
.nav li.active{color:var(--ink);font-weight:600}
.wordmark{left:142px;top:160px;font-family:"Lexend Exa",sans-serif;font-weight:400;font-size:58px;color:#fff;letter-spacing:2px}
.hero h1{position:absolute;left:142px;top:228px;font-family:"Lexend Exa",sans-serif;font-weight:300;font-size:35px;line-height:46px;color:#fff;letter-spacing:-1.5px}
.hero p{position:absolute;left:142px;top:338px;width:330px;font-size:10.5px;line-height:17px;color:#e3ebff}

/* about */
.about-photo{left:146px;top:656px;width:417px;height:399px;border-radius:12px;background:linear-gradient(135deg,#9aa3b0,#3a3f48 55%,#b9c0c9)}
.about h2{position:absolute;left:592px;top:666px;font-size:33px}
.about .body{position:absolute;left:592px;top:700px;width:400px;border-left:2px solid var(--green);padding-left:16px;font-size:10.5px;line-height:18px;color:var(--muted)}
.about .body ul{list-style:none;margin-top:8px;color:var(--ink)}
.about .body li{position:relative;padding-left:10px;margin-bottom:7px}
.about .body li:before{content:"";position:absolute;left:0;top:7px;width:4px;height:4px;border-radius:50%;background:var(--green)}
.years{left:592px;top:905px}
.years b{font-family:"Lexend Exa",sans-serif;font-size:32px;font-weight:700;letter-spacing:-2px}
.years span{display:block;font-size:9.5px;margin-top:2px}
.vsep{left:740px;top:915px;width:2px;height:40px;background:var(--green)}
.director{left:776px;top:912px;display:flex;gap:10px;align-items:center}
.avatar{width:40px;height:40px;border-radius:50%;background:#8e8e8e}
.director b{display:block;font-family:"Lexend Exa",sans-serif;font-weight:300;font-size:13px;color:#444}
.director span{font-size:12px;color:#555;font-family:"Lexend Exa",sans-serif;font-weight:300}

/* solutions */
.center-title{position:absolute;left:0;width:1133px;text-align:center;font-size:33px}
.card{position:absolute;top:1230px;width:273px;height:256px;border:2px solid #30c9a0;border-radius:8px;padding:22px 23px;background:#fff}
.card.featured{background:linear-gradient(135deg,#35e24a 0%,#23c87a 55%,#1769d6 100%);border:none;color:#fff}
.card svg{width:58px;height:58px}
.card h3{font-family:"Lexend Exa",sans-serif;font-weight:600;font-size:12px;margin-top:46px;letter-spacing:-.4px}
.card p{font-size:10px;line-height:18px;margin-top:16px;color:var(--muted)}
.card.featured p{color:#f1fff4}
.card a{display:block;font-family:"Lexend Exa",sans-serif;font-weight:600;font-size:9.5px;margin-top:16px;color:inherit}

/* expertise */
.expertise{position:absolute;left:0;top:1649px;width:1133px;height:499px;background:#eeeeee;overflow:hidden}
.exp-visual{position:absolute;left:0;top:0;width:573px;height:499px;background:radial-gradient(ellipse at 50% 65%,#2fb7ff 0%,#0d5fc0 35%,#062a6b 80%)}
.blob{position:absolute;border-radius:50%;background:linear-gradient(135deg,rgba(53,226,74,.25),rgba(23,105,214,.25))}
.exp-title{left:627px;top:60px;font-size:33px;line-height:36px}
.exp-item{position:absolute;left:627px;width:260px}
.exp-item .tick{position:absolute;left:0;top:0;width:14px;height:14px}
.exp-item h4{margin-left:40px;font-family:"Lexend Exa",sans-serif;font-weight:600;font-size:12px;letter-spacing:-.4px}
.exp-item p{margin:12px 0 0 40px;font-size:9px;line-height:12px;color:var(--muted)}

/* stories */
.story{position:absolute;background:#fff;border:1px solid var(--line);border-radius:8px;box-shadow:0 4px 16px rgba(0,0,0,.06)}
.story.side{opacity:.45}
.story .pic{position:absolute;background:linear-gradient(135deg,#d9dde3,#7d8592 60%,#e8eaee);border-radius:4px}
.story .info{position:absolute;font-size:9.5px;line-height:15px;color:var(--muted)}
.story .info .who{display:block;color:var(--ink);margin-top:6px}
.story .info ul{margin-left:12px;color:var(--ink)}
.story .info .k{color:var(--ink)}
.story .av{width:26px;height:26px;border-radius:50%;background:#555}
.arrow-btn{left:153px;top:2700px;width:22px;height:22px;border-radius:50%;background:var(--green)}
.dots{left:683px;top:2708px;display:flex;gap:6px}
.dots i{display:block;width:56px;height:4px;border-radius:2px;background:#eeeff2}
.dots i.on{background:linear-gradient(90deg,#1769d6,#35e24a)}
.stat{position:absolute;top:2770px;width:200px;margin-left:-100px;text-align:center}
.stat b{display:block;font-family:"Lexend Exa",sans-serif;font-weight:300;font-size:36px;letter-spacing:-2px;background:linear-gradient(90deg,#1769d6,#25c5a3);-webkit-background-clip:text;background-clip:text;color:transparent}
.stat i{display:block;width:26px;height:1px;background:#999;margin:14px auto 16px}
.stat span{font-size:10.5px}

/* local */
.globe{left:142px;top:2971px;width:462px;height:453px;border-radius:12px;background:radial-gradient(circle at 55% 45%,#2aa8ff 0%,#0c4fc0 40%,#04185a 85%)}
.local-card{position:absolute;left:560px;top:3041px;width:465px;height:320px;background:#fff;border:1px solid var(--line);box-shadow:0 4px 20px rgba(0,0,0,.06);padding:28px 34px}
.local-card h2{font-size:33px;line-height:36px}
.local-card p{margin-top:50px;font-size:12px;line-height:21px;width:360px}

/* contact */
.footer{position:absolute;left:0;top:3879px;width:1133px;height:469px;background:linear-gradient(180deg,#0c36c8 0%,#082aa0 45%,#06217e 100%)}
.map{left:211px;top:3599px;width:337px;height:323px;background:linear-gradient(135deg,#f3efe4,#e7ecf2);border:1px solid #dcdcdc;z-index:2}
.field{position:absolute;left:582px;width:342px;height:32px;background:var(--field);border-radius:3px;font-size:9.5px;padding:10px 16px;color:var(--ink);z-index:2}
.contact-item{position:absolute;top:3946px;display:flex;gap:10px;align-items:center;color:#fff;z-index:2}
.contact-item svg{width:34px;height:34px}
.contact-item b{display:block;font-family:"Lexend Exa",sans-serif;font-weight:600;font-size:12px}
.contact-item span{font-size:9px}
.f-brand{left:142px;top:4070px;display:flex;align-items:center;gap:14px;color:#fff;font-family:"Lexend Exa",sans-serif;font-weight:400;font-size:30px;letter-spacing:1px}
.f-brand .sq{width:42px;height:42px;border-radius:50%;background:var(--green)}
.socials{left:142px;top:4166px;display:flex;gap:10px}
.socials i{display:block;width:24px;height:24px;border-radius:50%;background:#fff}
.fcol{position:absolute;top:4056px;color:#fff}
.fcol h5{font-family:"Lexend Exa",sans-serif;font-weight:600;font-size:12px;margin-bottom:14px}
.fcol li{list-style:none;font-size:10px;margin-bottom:13px;color:#dfe7ff}
.divider{left:142px;top:4293px;width:849px;height:1px;background:rgba(255,255,255,.3)}
.copy{left:0;top:4312px;width:1133px;text-align:center;font-size:8.5px;color:#dfe7ff}
</style>
</head>
<body>
<div class="page">

  <!-- hero -->
  <section class="hero">
    <div class="hero-photo" role="img" aria-label="Two consultants in business attire looking at laptops over a blue network backdrop"></div>
    <nav class="nav">
      <div class="brand"><span class="brand-dot"></span>Velmora Systems GmbH</div>
      <ul>
        <li class="active">Home</li><li>About Us</li><li>Solutions ⌄</li><li>Markets Served</li><li>Success Stories</li><li>Contact Us</li>
      </ul>
    </nav>
    <div class="abs wordmark">VELMORA</div>
    <h1>Shaping the Future<br>of IT Consulting</h1>
    <p>Velmora Systems GmbH Helps Enterprises In Technology, Finance, And Energy Achieve Innovation, Reliability, And Growth Through Consulting, QA, And Test Automation</p>
    <div class="btn" style="left:142px;top:437px;width:218px;height:37px">Discover Our Expertise</div>
  </section>

  <!-- about -->
  <section class="about">
    <div class="abs about-photo" role="img" aria-label="Two engineers working together at a computer"></div>
    <h2 class="heading">About Velmora</h2>
    <div class="body">
      Lorem Ipsum Dolor Sit Amet Consectetur. Placerat Et Eget In Nisl. Neque Consectetur Scelerisque Aenean Sit. Dolor Accumsan Scelerisque Sed Vulputate Eget Cras Aliquam Turpis Sit. Nisi Pharetra Augue Ultricies Non Urna Amet Etiam. Vel Eleifend Neque Egestas Non Nec Nam Libero.
      <ul>
        <li>Lorem Ipsum Dolor Sit Amet Consectetur. Volutpat Mauris Tempor Nibh Nisi Volutpat Quis A Amet Eu.</li>
        <li>Lorem Ipsum Dolor Sit Amet Consectetur. Leo Sed Est Aliquet Ut Fermentum Accumsan. Sed Neque Aliquet Volutpat Augue Cursus Parturient Morbi. Ornare Arcu Pulvinar Tincidunt Cursus Pharetra Fames Potenti.</li>
      </ul>
    </div>
    <div class="abs years"><b>18+</b><span>Years Of Experiance</span></div>
    <div class="abs vsep"></div>
    <div class="abs director"><div class="avatar" role="img" aria-label="Portrait of the managing director"></div><div><b>Lena Hartwig</b><span>Managing Director</span></div></div>
    <div class="btn" style="left:592px;top:1017px;width:204px;height:37px">Discover More About</div>
  </section>

  <!-- solutions -->
  <h2 class="heading center-title" style="top:1140px">Tailored Solutions For Complex Challenges</h2>
  <article class="card featured" style="left:142px">
    <svg viewBox="0 0 58 58" fill="none" stroke="#fff" stroke-width="2"><path d="M16 30a9 9 0 0 1 2-17 12 12 0 0 1 22 3 8 8 0 0 1 2 14z"/><circle cx="29" cy="42" r="3"/><circle cx="14" cy="46" r="3"/><circle cx="44" cy="46" r="3"/><path d="M29 30v9M20 30l-5 13M38 30l5 13"/></svg>
    <h3>IT Consulting</h3>
    <p>Lorem Ipsum Dolor Sit Amet Consectetur. Viverra Pharetra Vitae Eu Est Fermentum Egestas Nec Rhoncus Cras. Nibh Cursus Mi.</p>
    <a>Read More</a>
  </article>
  <article class="card" style="left:431px">
    <svg viewBox="0 0 58 58" fill="none" stroke="#27b27a" stroke-width="2"><rect x="8" y="8" width="32" height="42" rx="3"/><path d="M16 20h16M16 28h10M16 36h8"/><circle cx="40" cy="38" r="9"/><path d="M36 38l3 3 5-6M47 45l6 6"/></svg>
    <h3>Quality Assurance &amp; Testing</h3>
    <p>Lorem Ipsum Dolor Sit Amet Consectetur. Viverra Pharetra Vitae Eu Est Fermentum Egestas Nec Rhoncus Cras. Nibh Cursus Mi.</p>
    <a>Read More</a>
  </article>
  <article class="card" style="left:719px">
    <svg viewBox="0 0 58 58" fill="none" stroke="#27b27a" stroke-width="2"><circle cx="22" cy="34" r="12"/><circle cx="22" cy="34" r="5"/><circle cx="42" cy="16" r="8"/><circle cx="42" cy="16" r="3"/><path d="M22 18v-4M22 54v-4M6 34h4M34 34h4M42 5v3M42 24v3M31 16h3M50 16h3"/></svg>
    <h3>Test Automation</h3>
    <p>Lorem Ipsum Dolor Sit Amet Consectetur. Viverra Pharetra Vitae Eu Est Fermentum Egestas Nec Rhoncus Cras. Nibh Cursus Mi.</p>
    <a>Read More</a>
  </article>
  <div class="btn" style="left:456px;top:1525px;width:220px;height:38px">Discover More Solution</div>

  <!-- expertise -->
  <section class="expertise">
    <div class="exp-visual" role="img" aria-label="Glowing blue data landscape with floating value markers"></div>
    <div class="blob" style="left:940px;top:-30px;width:200px;height:170px"></div>
    <div class="blob" style="left:960px;top:340px;width:220px;height:200px"></div>
    <div class="blob" style="left:800px;top:400px;width:120px;height:110px"></div>
    <h2 class="heading abs exp-title">Expertise<br>Across Sectors</h2>
    <div class="exp-item" style="top:158px">
      <svg class="tick" viewBox="0 0 14 14" fill="none" stroke="#35c24a" stroke-width="1.3"><circle cx="7" cy="7" r="6"/><path d="M4 7h6M7.5 4.5L10 7l-2.5 2.5"/></svg>
      <h4>Technology</h4><p>dolor sit amet consectetur. Ac quis odio odio enim. Nulla tortor et sollicitudin lorem.</p>
    </div>
    <div class="exp-item" style="top:232px">
      <svg class="tick" viewBox="0 0 14 14" fill="none" stroke="#35c24a" stroke-width="1.3"><circle cx="7" cy="7" r="6"/><path d="M4 7h6M7.5 4.5L10 7l-2.5 2.5"/></svg>
      <h4>Finance</h4><p>Lorem ipsum dolor sit amet consectetur. In ipsum semper vestibulum dignissim nisi.</p>
    </div>
    <div class="exp-item" style="top:306px">
      <svg class="tick" viewBox="0 0 14 14" fill="none" stroke="#35c24a" stroke-width="1.3"><circle cx="7" cy="7" r="6"/><path d="M4 7h6M7.5 4.5L10 7l-2.5 2.5"/></svg>
      <h4>Energy</h4><p>Lorem ipsum dolor sit amet consectetur. Dignissim quis tincidunt.</p>
    </div>
    <div class="btn" style="left:627px;top:369px;width:240px;height:35px">Get Start With Our Expert</div>
  </section>

  <!-- stories -->
  <h2 class="heading center-title" style="top:2250px">Proven Impact, Measurable Results.</h2>
  <div class="story side" style="left:142px;top:2394px;width:165px;height:175px">
    <div class="pic" style="left:8px;top:8px;width:130px;height:158px" role="img" aria-label="Team meeting in an office"></div>
  </div>
  <div class="story side" style="left:840px;top:2394px;width:185px;height:175px">
    <div class="info" style="left:16px;top:12px;width:150px;font-size:6px;line-height:10px"><div class="av" style="width:14px;height:14px"></div><span class="who">Ben Carlow</span>Short client note on project.<br>City: USA<br>Company: Northline<br>Goals: faster test cycles</div>
    <div class="btn" style="left:16px;top:140px;width:100px;height:18px;font-size:6px">View More Details</div>
  </div>
  <div class="story" style="left:304px;top:2320px;width:527px;height:320px">
    <div class="pic" style="left:16px;top:20px;width:226px;height:275px" role="img" aria-label="Business team reviewing documents at a meeting table"></div>
    <div class="info" style="left:258px;top:26px;width:250px">
      <div class="av" role="img" aria-label="Client portrait"></div>
      <span class="who">Mara Ellison</span>
      Lorem ipsum dolor sit amet consectetur. Consequat sed nisl adipiscing quis. Nec morbi nulla mi quis tellus arcu dictumst lectus id.<br>
      <span class="k">City:</span> USA<br>
      <span class="k">Company:</span> Northline<br>
      <span class="k">Goals:</span>
      <ul><li>Lorem ipsum dolor sit amet consectetur. In neque pretium ultrices elit</li><li>in pharetra ac nec est. Sed nulla eu vitae sit.</li></ul>
    </div>
    <div class="btn" style="left:258px;top:255px;width:182px;height:35px">View More Details</div>
  </div>
  <svg class="abs arrow-btn" viewBox="0 0 22 22"><circle cx="11" cy="11" r="11" fill="#35e24a"/><path d="M15 11H7M10 7.5L6.5 11 10 14.5" stroke="#fff" stroke-width="1.6" fill="none"/></svg>
  <div class="abs dots"><i class="on"></i><i></i><i></i><i></i><i></i></div>

  <div class="stat" style="left:240px"><b>98%</b><i></i><span>Software Reliability Rate</span></div>
  <div class="stat" style="left:453px"><b>+217%</b><i></i><span>Test Automation Coverage</span></div>
  <div class="stat" style="left:668px"><b>100k+</b><i></i><span>Global Projects Delivered</span></div>
  <div class="stat" style="left:886px"><b>500+</b><i></i><span>Consulting Success Stories</span></div>

  <!-- local roots -->
  <div class="abs globe" role="img" aria-label="Glowing blue globe with network connections"></div>
  <div class="local-card">
    <h2 class="heading">Local Roots,<br>Global Reach</h2>
    <p>With Offices In Germany And Strong Presence In The U.S., Velmora Systems Serves Clients Worldwide With Premium IT Solutions.</p>
    <div class="btn" style="left:34px;top:242px;width:136px;height:37px">Get Started</div>
  </div>

  <!-- contact + footer -->
  <h2 class="heading center-title" style="top:3520px">Get In Touch With Us</h2>
  <footer class="footer"></footer>
  <div class="abs map" role="img" aria-label="Street map of the office location with a location pin"></div>
  <div class="field" style="top:3599px">Name</div>
  <div class="field" style="top:3649px">Mobile Phone</div>
  <div class="field" style="top:3700px">Email</div>
  <div class="field" style="top:3747px;height:168px">Message</div>
  <div class="btn" style="left:582px;top:3941px;width:342px;height:35px;z-index:2">Submit Now</div>

  <div class="contact-item" style="left:211px">
    <svg viewBox="0 0 34 34" fill="none" stroke="#fff" stroke-width="1.5"><rect x="3" y="9" width="28" height="19" rx="2"/><path d="M3 11l14 10 14-10"/></svg>
    <div><b>Email Us</b><span>info@velmora-systems.example</span></div>
  </div>
  <div class="contact-item" style="left:430px">
    <svg viewBox="0 0 34 34" fill="none" stroke="#fff" stroke-width="1.5"><path d="M8 4l5 1 2 7-3 3a18 18 0 0 0 8 8l3-3 7 2 1 5c-1 3-4 4-7 3C15 27 8 20 5 11 4 8 5 5 8 4z"/></svg>
    <div><b>Phone</b><span>555-014-2290</span></div>
  </div>

  <div class="abs f-brand"><span class="sq"></span>Velmora Systems GmbH</div>
  <div class="abs socials"><i></i><i></i><i></i><i></i></div>
  <div class="fcol" style="left:666px"><h5>Quick Links</h5><ul><li>Home</li><li>About Us</li><li>Markets Served</li><li>Solutions</li><li>Success Stories</li></ul></div>
  <div class="fcol" style="left:850px"><h5>Product Solution</h5><ul><li>Test Automation</li><li>IT Consulting</li><li>Quality Assurance &amp; Testing</li></ul></div>
  <div class="abs divider"></div>
  <div class="abs copy">Copyright 2025 . All Rights Reserved</div>
</div>
</body>
</html>
```